VELMIRAN (coffee package design)

Make coffee bag for coffee beans: VELMIRAN is a quality-driven coffee roaster focused on crafting fresh, flavorful coffee from premium beans sourced directly from farms. We build close relationships with growers to ensure ethical practices, traceability, and exceptional quality at the origin. Our small-batch roasting approach brings out the unique character of each bean—highlighting bold notes, rich complexity, and peak freshness. At VELMIRAN, we believe great coffee starts at the source—and ends in your cup, roasted to perfection.

**VELMIRAN** is a quality-driven coffee roaster focused on crafting fresh, flavorful coffee from **premium beans sourced directly from farms**. We build close relationships with growers to ensure ethical practices, traceability, and exceptional quality at the origin. Our small-batch roasting approach brings out the unique character of each bean—highlighting bold notes, rich complexity, and peak freshness. At **VELMIRAN**, we believe great coffee starts at the source—and ends in your cup, roasted to perfection.

VELMIRAN

ETHICALLY SOURCED COFFEE

On Top: 100% Arabica Beans

On Left Side:
Coffee brew guide: https://in.brewboardly.com/pin/318274659201847362/
https://in.brewboardly.com/pin/coffee-brewing-method-chart--207431985562143/

On right side bottom:
STORAGE
Proper storage is essential to maintaining your coffee’s freshness and flavor. Once opened, we recommend keeping your coffee in a cool, dark, dry place and sealed in an airtight container. Always reseal the bag after each use to preserve maximum freshness and aroma.

487 Tullane Street Brennick Vale 10482

Follow Us
www.velmiran.com
TikTok@velmiran
IG@getvelmiran

Target Market(s)

Coffee/ Cafe

Industry/Entity Type

Coffee

Font styles to use
Other font styles liked:
• Non‑Seasonal Sans

Requirements
Must have
• Clean, modern
Nice to have
• Elegant

```html
<!DOCTYPE html>
<html lang="en">
<head>
<meta charset="utf-8">
<title>VELMIRAN – Coffee Bag Dieline</title>
<link href="https://fonts.googleapis.com/css2?family=Playfair+Display:wght@500;700&family=Oswald:wght@600;700&family=Great+Vibes&family=Montserrat:wght@400;600;700&display=swap" rel="stylesheet">
<style>
  :root {
    --roast-dark: #2a0d0d;
    --roast-mid: #5a1c1c;
    --roast-deep: #1a0707;
    --cream: #f6efe6;
    --paper: #ffffff;
    --gold-light: #e2bf7a;
    --ink: #2b1a17;
    --muted: #6d5a55;
    --line: #d9cfc8;
  }
  * { box-sizing: border-box; margin: 0; padding: 0; }
  html, body { width: 878px; height: 1200px; overflow: hidden; background: var(--cream); }
  body { font-family: "Montserrat", sans-serif; color: var(--ink); }

  .dieline { display: flex; width: 878px; height: 1200px; }
  .panel { height: 100%; position: relative; overflow: hidden; }

  /* Brew guide */
  .panel--guide { width: 200px; background: var(--paper); border-right: 1px solid var(--line); padding: 24px 14px; }
  .guide-title { background: var(--roast-dark); color: var(--paper); font: 700 11px "Montserrat", sans-serif; letter-spacing: 1px; padding: 9px 10px; margin-bottom: 18px; white-space: nowrap; }
  .brew { display: flex; gap: 10px; align-items: center; padding: 12px 0; border-bottom: 1px solid var(--line); }
  .brew-art { width: 56px; height: 70px; flex: none; border-radius: 4px; background: linear-gradient(160deg, #e9e2dc, #bfb2aa); }
  .brew-name { font: 700 10px "Montserrat", sans-serif; letter-spacing: 1px; color: var(--roast-mid); margin-bottom: 5px; white-space: nowrap; }
  .brew-spec { font-size: 9px; line-height: 1.6; color: var(--muted); }

  /* Front */
  .panel--front { width: 260px; background: linear-gradient(180deg, #f4ece6 0%, #c9a8a0 14%, var(--roast-mid) 32%, var(--roast-dark) 70%, var(--roast-deep) 100%); text-align: center; }
  .seal { position: absolute; top: 40px; left: 50%; transform: translateX(-50%); width: 74px; height: 74px; border-radius: 50%; background: var(--paper); border: 3px solid var(--roast-mid); display: flex; align-items: center; justify-content: center; font: 700 19px "Oswald", sans-serif; color: var(--roast-dark); }
  .front-brand { position: absolute; top: 300px; width: 100%; font: 700 30px "Playfair Display", serif; letter-spacing: 2px; color: var(--paper); }
  .front-claim { position: absolute; top: 380px; width: 100%; font: 700 40px/1 "Oswald", sans-serif; letter-spacing: 1px; }
  .front-claim .claim-a { color: var(--paper); display: block; }
  .front-claim .claim-b { color: var(--gold-light); display: block; }
  .front-script { position: absolute; top: 462px; width: 100%; font: 58px "Great Vibes", cursive; color: var(--paper); }
  .front-meta { position: absolute; top: 545px; width: 100%; font-size: 10px; line-height: 1.6; color: var(--cream); letter-spacing: .5px; }
  .front-beans { position: absolute; bottom: 0; left: 0; width: 100%; height: 420px; background: radial-gradient(ellipse at 50% 80%, #4a2418 0%, #2a120b 55%, transparent 100%); }

  /* Storage side */
  .panel--storage { width: 170px; background: linear-gradient(180deg, var(--paper) 0%, var(--paper) 58%, var(--roast-mid) 80%, var(--roast-dark) 100%); border-left: 1px solid var(--line); border-right: 1px solid var(--line); padding: 260px 16px 0; }
  .storage-tab { display: inline-block; background: var(--roast-dark); color: var(--paper); font: 700 12px "Montserrat", sans-serif; letter-spacing: 2px; padding: 6px 12px; margin-bottom: 14px; }
  .storage-text { font-size: 9.5px; line-height: 1.65; color: var(--ink); margin-bottom: 16px; }
  .storage-address { display: flex; gap: 6px; font-size: 9px; line-height: 1.5; color: var(--ink); margin-bottom: 16px; }
  .storage-address svg { flex: none; margin-top: 1px; }
  .follow-title { font: 700 10px "Montserrat", sans-serif; letter-spacing: 1px; color: var(--roast-mid); margin-bottom: 6px; }
  .follow-list { list-style: none; font-size: 9px; line-height: 1.8; color: var(--ink); }

  /* Back */
  .panel--back { width: 248px; background: linear-gradient(180deg, var(--roast-mid) 0%, var(--roast-dark) 45%, var(--roast-deep) 100%); color: var(--cream); padding: 120px 22px 0; text-align: center; }
  .back-heading { font: 700 15px/1.4 "Montserrat", sans-serif; letter-spacing: 1px; color: var(--paper); margin-bottom: 18px; white-space: nowrap; }
  .back-text { font-size: 10px; line-height: 1.75; color: #e6d6cd; text-align: left; }
  .back-brand { position: absolute; bottom: 170px; left: 0; width: 100%; font: 700 24px "Playfair Display", serif; letter-spacing: 2px; color: var(--paper); }
</style>
</head>
<body>
<main class="dieline">

  <section class="panel panel--guide">
    <h2 class="guide-title">COFFEE BREW GUIDE</h2>
    <div class="brew"><div class="brew-art" role="img" aria-label="Coffee dripper line illustration"></div><div><p class="brew-name">COFFEE DRIPPER</p><p class="brew-spec">Ratio 1:16<br>Grind Medium<br>Time 3 min</p></div></div>
    <div class="brew"><div class="brew-art" role="img" aria-label="French press line illustration"></div><div><p class="brew-name">FRENCH PRESS</p><p class="brew-spec">Ratio 1:15<br>Grind Coarse<br>Time 4 min</p></div></div>
    <div class="brew"><div class="brew-art" role="img" aria-label="Press brewer line illustration"></div><div><p class="brew-name">PRESS BREWER</p><p class="brew-spec">Ratio 1:12<br>Grind Fine<br>Time 2 min</p></div></div>
    <div class="brew"><div class="brew-art" role="img" aria-label="Moka pot line illustration"></div><div><p class="brew-name">MOKA POT</p><p class="brew-spec">Ratio 1:10<br>Grind Fine<br>Time 5 min</p></div></div>
    <div class="brew"><div class="brew-art" role="img" aria-label="Pour over carafe line illustration"></div><div><p class="brew-name">POUR OVER</p><p class="brew-spec">Ratio 1:17<br>Grind Medium<br>Time 4 min</p></div></div>
    <div class="brew"><div class="brew-art" role="img" aria-label="Siphon brewer line illustration"></div><div><p class="brew-name">SIPHON</p><p class="brew-spec">Ratio 1:15<br>Grind Medium<br>Time 2 min</p></div></div>
  </section>

  <section class="panel panel--front">
    <div class="seal">100%</div>
    <h1 class="front-brand">VELMIRAN</h1>
    <p class="front-claim"><span class="claim-a">ETHICALLY</span><span class="claim-b">SOURCED</span></p>
    <p class="front-script">Coffee</p>
    <p class="front-meta">100% Arabica Beans<br>Net Wt 12 oz</p>
    <div class="front-beans" role="img" aria-label="Photograph of roasted coffee beans"></div>
  </section>

  <section class="panel panel--storage">
    <h2 class="storage-tab">STORAGE</h2>
    <p class="storage-text">Proper storage is essential to maintaining your coffee’s freshness and flavor. Once opened, we recommend keeping your coffee in a cool, dark, dry place and sealed in an airtight container. Always reseal the bag after each use to preserve maximum freshness and aroma.</p>
    <p class="storage-address">
      <svg width="10" height="13" viewBox="0 0 10 13" aria-hidden="true"><path d="M5 0a5 5 0 0 1 5 5c0 3.5-5 8-5 8S0 8.5 0 5a5 5 0 0 1 5-5z" fill="#5a1c1c"/><circle cx="5" cy="5" r="1.8" fill="#fff"/></svg>
      <span>487 Tullane Street Brennick Vale 10482</span>
    </p>
    <h3 class="follow-title">Follow Us</h3>
    <ul class="follow-list">
      <li>www.velmiran.com</li>
      <li>TikTok@velmiran</li>
      <li>IG@getvelmiran</li>
    </ul>
  </section>

  <section class="panel panel--back">
    <h2 class="back-heading">FROM FARM TO CUP,<br>WITH CARE</h2>
    <p class="back-text">At Velmiran, every bag begins with growers we know by name. We source premium beans directly from farms, roast them in small batches, and pack them at peak freshness so bold notes and rich complexity reach your cup exactly as the origin intended.</p>
    <p class="back-brand">VELMIRAN</p>
  </section>

</main>
</body>
</html>
```